stationary and business card
varkomo.de - online services platform
Project: stationary and business card
stationary and business card - Internet Services
Creative Brief
Modern
Dipl. Inf. Tobias Wendrich
Luvesor
Ulmenhain Str. 14 70386 Weil der Stadt
tobias.wendrich@mailhafen.de
www.varkomo.de
Please use logo colors, and see the following flyer to fit the style: varkomo.de/flyer.pdf
Für Dienstleister: * Kostenlose reservierungsplatform * Kostengunstige Flyer-Werbung * Kosten und Zeit für Anreise gleich bei Reservierung berechnen * Eigene varkomo.de Subdomain und Web- Seite mit einem SSL Zertifi kat * SMS Benachrichtigungen bei Reservierung 24 h Für Kunden: * 24 Stunden täglich online reservieren (z.B. Arzt, Massage, Friseur, uvm.) * Schnelle Abwicklung * Last-Minute-Preise und Frübucherrabatt möglich * Bewertungssystem für zuverlässige Dienstleister

```html
<!DOCTYPE html>
<html lang="de">
<head>
<meta charset="utf-8">
<title>varkomo.de – Briefpapier und Visitenkarten</title>
<link href="https://fonts.googleapis.com/css2?family=Open+Sans:wght@400;600;700&display=swap" rel="stylesheet">
<style>
  :root {
    --bg: #3a3d42;
    --paper: #ffffff;
    --blue: #1d9ad8;
    --blue-dark: #0b6eaf;
    --blue-light: #8fd6f6;
    --green: #7cc142;
    --ink: #4a4f55;
    --ink-soft: #8a9096;
    --rule: #c9ced3;
  }
  * { box-sizing: border-box; margin: 0; padding: 0; }
  html, body { width: 1200px; height: 482px; overflow: hidden; }
  body { background: var(--bg); font-family: "Open Sans", Arial, sans-serif; color: var(--ink); position: relative; }

  .sheet, .envelope, .card { position: absolute; background: var(--paper); overflow: hidden; }

  /* shared pieces */
  .side-band { position: absolute; left: 0; top: 0; bottom: 0; width: 12px;
    background: linear-gradient(180deg, var(--blue-light), var(--blue) 45%, var(--blue-dark)); }
  .brand { position: absolute; display: flex; align-items: center; gap: 5px; }
  .brand-dot { border-radius: 50%; background: var(--blue); flex: none; }
  .brand-name { font-weight: 700; color: var(--blue); line-height: 1; }
  .brand-tag { position: absolute; font-size: 4px; color: var(--ink-soft); }
  .footer-address { position: absolute; font-size: 4.5px; line-height: 1.55; color: var(--ink); }

  /* letterhead */
  .letterhead { left: 19px; top: 29px; width: 288px; height: 422px; }
  .letterhead .brand { left: 22px; top: 12px; }
  .letterhead .brand-dot { width: 18px; height: 18px; }
  .letterhead .brand-name { font-size: 20px; }
  .letterhead .brand-tag { left: 45px; top: 34px; }
  .watermark-circle { position: absolute; left: 54px; top: 104px; width: 180px; height: 180px;
    border-radius: 50%; background: radial-gradient(circle, rgba(29,154,216,0.10), rgba(29,154,216,0.04)); }
  .letterhead .footer-address { left: 22px; bottom: 16px; }

  /* fax */
  .fax { left: 329px; top: 29px; width: 283px; height: 422px; }
  .fax .brand { left: 22px; top: 12px; }
  .fax .brand-dot { width: 18px; height: 18px; }
  .fax .brand-name { font-size: 20px; }
  .fax .brand-tag { left: 45px; top: 34px; }
  .fax-title { position: absolute; left: 22px; top: 62px; font-size: 22px; font-weight: 400; color: #222; letter-spacing: 0.5px; }
  .fax-fields { position: absolute; left: 22px; top: 94px; width: 244px; display: grid; grid-template-columns: 1fr 1fr; column-gap: 12px; row-gap: 6px; }
  .fax-field { font-size: 5px; color: var(--ink-soft); border-bottom: 0.6px solid var(--rule); padding-bottom: 2px; height: 10px; }
  .fax-rule { position: absolute; left: 22px; width: 244px; height: 1.5px; background: var(--rule); }
  .fax-options { position: absolute; left: 22px; top: 176px; width: 244px; display: flex; justify-content: space-between; }
  .fax-option { display: flex; align-items: center; gap: 2px; font-size: 4.5px; color: var(--ink); }
  .fax-option::before { content: ""; width: 5px; height: 5px; border: 0.6px solid var(--ink-soft); }
  .fax .footer-address { left: 22px; bottom: 16px; }

  /* envelopes */
  .envelope-back { left: 684px; top: 24px; width: 499px; height: 178px; }
  .envelope-back svg { position: absolute; inset: 0; }
  .envelope-back .flap-dot { position: absolute; left: 240px; top: 82px; width: 20px; height: 20px; border-radius: 50%; background: var(--blue); }
  .envelope-front { left: 660px; top: 139px; width: 480px; height: 173px; box-shadow: 0 -2px 6px rgba(0,0,0,0.18); }
  .envelope-front .brand { left: 24px; top: 14px; }
  .envelope-front .brand-dot { width: 14px; height: 14px; }
  .envelope-front .brand-name { font-size: 15px; }
  .envelope-front .brand-tag { left: 43px; top: 32px; }
  .envelope-front .footer-address { left: 24px; top: 52px; }
  .envelope-front .envelope-web { position: absolute; left: 24px; bottom: 12px; font-size: 4.5px; font-weight: 600; color: var(--ink); }
  .envelope-front .bottom-band { position: absolute; left: 0; right: 0; bottom: 0; height: 6px; background: linear-gradient(90deg, var(--blue-dark), var(--blue), var(--blue-light)); }

  /* business cards */
  .card { top: 360px; height: 86px; border-radius: 3px; }
  .card-front { left: 715px; width: 144px; }
  .card-front .brand { left: 14px; top: 12px; }
  .card-front .brand-dot { width: 10px; height: 10px; }
  .card-front .brand-name { font-size: 11px; }
  .card-front .bottom-band { position: absolute; left: 0; right: 0; bottom: 0; height: 20px; background: linear-gradient(90deg, var(--blue-dark), var(--blue), var(--blue-light)); }
  .card-front .card-web { position: absolute; right: 8px; bottom: 6px; font-size: 5px; color: #fff; font-weight: 600; }

  .card-contact { left: 869px; width: 144px; }
  .card-contact .side-band { width: 8px; }
  .card-contact .person { position: absolute; left: 16px; top: 10px; }
  .person-name { font-size: 6px; font-weight: 700; color: var(--blue); }
  .person-role { font-size: 4px; color: var(--ink-soft); margin-bottom: 6px; }
  .contact-line { font-size: 4.2px; line-height: 1.6; color: var(--ink); }

  .card-services { left: 1027px; width: 149px; background: linear-gradient(135deg, var(--blue-dark), var(--blue) 60%, var(--blue-light)); color: #fff; }
  .card-services .services { position: absolute; left: 10px; top: 9px; right: 10px; }
  .services h3 { font-size: 5px; font-weight: 700; margin-bottom: 2px; }
  .services ul { list-style: none; font-size: 3.8px; line-height: 1.5; margin-bottom: 5px; }
  .services li::before { content: "• "; }
</style>
</head>
<body>

<section class="sheet letterhead" aria-label="Briefbogen">
  <div class="side-band"></div>
  <div class="brand"><span class="brand-dot"></span><span class="brand-name">varkomo.de</span></div>
  <div class="brand-tag">Ihr Online-Dienstleister</div>
  <div class="watermark-circle"></div>
  <address class="footer-address">
    Ulmenhain Str. 14<br>70386 Weil der Stadt<br><br>
    tobias.wendrich@mailhafen.de<br><strong>www.varkomo.de</strong>
  </address>
</section>

<section class="sheet fax" aria-label="Faxvorlage">
  <div class="side-band"></div>
  <div class="brand"><span class="brand-dot"></span><span class="brand-name">varkomo.de</span></div>
  <div class="brand-tag">Ihr Online-Dienstleister</div>
  <h1 class="fax-title">FAX</h1>
  <div class="fax-fields">
    <div class="fax-field">To:</div><div class="fax-field">From:</div>
    <div class="fax-field">Fax:</div><div class="fax-field">Pages:</div>
    <div class="fax-field">Phone:</div><div class="fax-field">Date:</div>
    <div class="fax-field">Re:</div><div class="fax-field">CC:</div>
  </div>
  <div class="fax-rule" style="top:166px"></div>
  <div class="fax-options">
    <span class="fax-option">Urgent</span>
    <span class="fax-option">For Review</span>
    <span class="fax-option">Please Comment</span>
    <span class="fax-option">Please Reply</span>
    <span class="fax-option">Please Recycle</span>
  </div>
  <address class="footer-address">
    Ulmenhain Str. 14<br>70386 Weil der Stadt<br><br>
    tobias.wendrich@mailhafen.de<br><strong>www.varkomo.de</strong>
  </address>
</section>

<section class="envelope envelope-back" aria-label="Briefumschlag Rückseite">
  <svg width="499" height="178" viewBox="0 0 499 178">
    <defs>
      <linearGradient id="flapBand" x1="0" x2="1">
        <stop offset="0" stop-color="var(--blue-dark)"/><stop offset="1" stop-color="var(--blue-light)"/>
      </linearGradient>
    </defs>
    <rect x="0" y="0" width="499" height="8" fill="url(#flapBand)"/>
    <polyline points="0,8 250,96 499,8" fill="none" stroke="#d5dade" stroke-width="1.2"/>
  </svg>
  <div class="flap-dot"></div>
</section>

<section class="envelope envelope-front" aria-label="Briefumschlag Vorderseite">
  <div class="side-band" style="width:8px"></div>
  <div class="brand"><span class="brand-dot"></span><span class="brand-name">varkomo.de</span></div>
  <div class="brand-tag">Ihr Online-Dienstleister</div>
  <address class="footer-address">Ulmenhain Str. 14 · 70386 Weil der Stadt</address>
  <div class="envelope-web">www.varkomo.de</div>
  <div class="bottom-band"></div>
</section>

<section class="card card-front" aria-label="Visitenkarte Vorderseite">
  <div class="brand"><span class="brand-dot"></span><span class="brand-name">varkomo.de</span></div>
  <div class="bottom-band"></div>
  <div class="card-web">www.varkomo.de</div>
</section>

<section class="card card-contact" aria-label="Visitenkarte Kontakt">
  <div class="side-band"></div>
  <div class="person">
    <div class="person-name">Tobias Wendrich</div>
    <div class="person-role">Dipl. Inf. · Luvesor</div>
    <div class="contact-line">Ulmenhain Str. 14</div>
    <div class="contact-line">70386 Weil der Stadt</div>
    <div class="contact-line">tobias.wendrich@mailhafen.de</div>
    <div class="contact-line">www.varkomo.de</div>
  </div>
</section>

<section class="card card-services" aria-label="Visitenkarte Leistungen">
  <div class="services">
    <h3>Für Dienstleister</h3>
    <ul>
      <li>Kostenlose Reservierungsplattform</li>
      <li>SMS Benachrichtigungen 24 h</li>
    </ul>
    <h3>Für Kunden</h3>
    <ul>
      <li>24 Stunden täglich online reservieren</li>
      <li>Bewertungssystem für Dienstleister</li>
    </ul>
  </div>
</section>

</body>
</html>
```